Fahrzeugbeschriftung für Vertrieb von mechanischen und elektronischen Schließanlagen
Man muss glaube ich nicht viel zum Designer sagen, wenn man sich das Ergebnis betrachtet! Wir sind SEHR zufrieden. Kommunikation und Reaktionsgeschwindigkeit sind vorbildlich! Immer wieder gern!
Zielgruppe
Vertrieb von mechanischen und elektronischen Schließanlagen
Aufgabenstellung
in den Bildern ist ein Beispiel einer Folierung, diese dient ein wenig als Muster! wir wollen ein Dunkles Design mit großen Akzenten unseres Logos und Schriftzugs (Gern auch über Kante oder Dach) Das Logo sollte schon groß sein. Ebenso wollen wir einige Logos unserer Lieferanten auf dem Fahrzeug platzieren - diese jedoch etwas dezenter.
Auto ist ein KM Q8.3 Transporter

```html
<!DOCTYPE html>
<html lang="de">
<head>
<meta charset="utf-8">
<title>Riegelhaus Franken – Fahrzeugbeschriftung</title>
<link rel="stylesheet" href="https://fonts.googleapis.com/css2?family=Exo+2:ital,wght@0,300;1,700;1,900&display=swap">
<style>
  :root {
    --stage-light: #c9c9c9;
    --stage-dark: #8e8e8e;
    --wrap-black: #000000;
    --band-grey: #5a5a5a;
    --band-grey-dark: #3e3e3e;
    --stripe-white: #f2f2f2;
    --stripe-grey: #cfcfcf;
    --brand-sand: #bdbcae;
    --metal-light: #e6e4d6;
    --metal-dark: #8d8b7a;
    --text-white: #ffffff;
    --partner-red: #e0141b;
    --partner-light: #d9d9d9;
    --partner-blue: #3d8fd1;
    --dot-tone: #6f6f68;
  }
  html, body {
    margin: 0;
    width: 1200px;
    height: 1117px;
    overflow: hidden;
  }
  body {
    background: linear-gradient(135deg, var(--stage-light), var(--stage-dark));
    display: flex;
    align-items: center;
    justify-content: center;
    font-family: "Exo 2", sans-serif;
  }
  .wrap-layout {
    width: 1120px;
    height: 397px;
    display: block;
  }
  .brand-name {
    font-family: "Exo 2", sans-serif;
    font-weight: 300;
    fill: var(--brand-sand);
  }
  .headline-text {
    font-family: "Exo 2", sans-serif;
    font-weight: 900;
    font-style: italic;
  }
  .headline-top { fill: var(--text-white); stroke: #000; stroke-width: 4; paint-order: stroke; }
  .headline-mid { fill: url(#metal); stroke: #000; stroke-width: 4; paint-order: stroke; }
  .headline-sub { fill: var(--text-white); }
  .web-address {
    font-family: "Exo 2", sans-serif;
    font-weight: 700;
    font-style: italic;
    fill: var(--text-white);
  }
</style>
</head>
<body>
<svg class="wrap-layout" viewBox="0 0 1732 614" xmlns="http://www.w3.org/2000/svg" aria-label="Seitenansicht der Fahrzeugfolierung Riegelhaus Franken">
  <defs>
    <linearGradient id="metal" x1="0" y1="0" x2="0" y2="1">
      <stop offset="0" stop-color="var(--metal-light)"/>
      <stop offset="0.55" stop-color="var(--metal-dark)"/>
      <stop offset="1" stop-color="var(--metal-light)"/>
    </linearGradient>
    <linearGradient id="stripe" x1="0" y1="0" x2="1" y2="1">
      <stop offset="0" stop-color="var(--stripe-white)"/>
      <stop offset="1" stop-color="var(--stripe-grey)"/>
    </linearGradient>
    <linearGradient id="band" x1="0" y1="0" x2="1" y2="0">
      <stop offset="0" stop-color="var(--band-grey)"/>
      <stop offset="1" stop-color="var(--band-grey-dark)"/>
    </linearGradient>
    <linearGradient id="dotfield-right" x1="0" y1="0" x2="1" y2="0">
      <stop offset="0" stop-color="var(--dot-tone)" stop-opacity="0"/>
      <stop offset="0.6" stop-color="var(--dot-tone)" stop-opacity="0.45"/>
      <stop offset="1" stop-color="var(--dot-tone)" stop-opacity="0.1"/>
    </linearGradient>
    <linearGradient id="dotfield-left" x1="0" y1="0" x2="0" y2="1">
      <stop offset="0" stop-color="var(--dot-tone)" stop-opacity="0"/>
      <stop offset="1" stop-color="var(--dot-tone)" stop-opacity="0.45"/>
    </linearGradient>
  </defs>

  <rect class="wrap-base" width="1732" height="614" fill="var(--wrap-black)"/>

  <g class="speed-stripes">
    <polygon points="1017,0 1152,0 1250,219 1130,219" fill="url(#stripe)"/>
    <polygon points="1172,0 1207,0 1305,194 1270,194" fill="url(#stripe)"/>
  </g>

  <rect class="dot-field" role="img" aria-label="Dekoratives Punktraster" x="1450" y="370" width="280" height="244" fill="url(#dotfield-right)"/>

  <polygon class="headline-band" points="772,309 1732,129 1682,359 1250,440 1300,528 922,588" fill="url(#band)"/>

  <rect class="dot-field" role="img" aria-label="Dekoratives Punktraster" x="760" y="490" width="220" height="124" fill="url(#dotfield-left)"/>

  <polygon class="lower-sweep" points="557,614 1297,514 1337,614" fill="url(#stripe)"/>

  <g class="brand-mark">
    <circle cx="620" cy="352" r="62" fill="none" stroke="var(--brand-sand)" stroke-width="6"/>
    <text class="brand-name" x="620" y="470" font-size="34" text-anchor="middle" textLength="240" lengthAdjust="spacingAndGlyphs">RIEGELHAUS</text>
    <text class="brand-name" x="620" y="520" font-size="50" text-anchor="middle" textLength="240" lengthAdjust="spacingAndGlyphs">FRANKEN</text>
  </g>

  <text class="web-address" x="1335" y="179" font-size="21" textLength="310" lengthAdjust="spacingAndGlyphs" transform="rotate(-10.2 1335 179)">www.riegelhaus-franken.de</text>

  <g class="headline">
    <text class="headline-text headline-top" x="867" y="369" font-size="86" textLength="838" lengthAdjust="spacingAndGlyphs" transform="rotate(-10.3 867 369)">MECHANISCHEN UND</text>
    <text class="headline-text headline-mid" x="877" y="426" font-size="86" textLength="705" lengthAdjust="spacingAndGlyphs" transform="rotate(-10.6 877 426)">ELEKTRONISCHEN</text>
    <text class="headline-text headline-sub" x="1130" y="429" font-size="40" textLength="404" lengthAdjust="spacingAndGlyphs" transform="rotate(-10.5 1130 429)">SCHLIEßANLAGEN</text>
  </g>

  <g class="partner-badges">
    <rect x="907" y="472" width="60" height="32" rx="3" fill="var(--partner-blue)"/>
    <rect x="983" y="474" width="66" height="30" rx="6" fill="var(--partner-red)"/>
    <rect x="1064" y="481" width="110" height="16" rx="3" fill="var(--partner-light)"/>
    <rect x="1190" y="472" width="32" height="32" rx="3" fill="var(--partner-red)"/>
  </g>
</svg>
</body>
</html>
```